Hawaiian skin care product needs label design

We are looking for a font for Hawaiian skin care product called 'omu - which means 'skin' in Hawaiian.
No need for a logo or a mark, simply looking for a clean, fresh, modern, young, and crisp font and background for our product label.
We are creating the label for the product bag, see file attached for reference.
Ideas we like: Subtle gradient water color back ground, fade chevron, see files attached.
This is a women's product, but don't want it to be too feminine or overly girly. Fresh and crisp, modern with subtle undertones of femininity.
Updates

Reason: Need to have the back of the label created as well.

Target Market(s)

Women, ages 18-40 Up scale, modern, hip. Mature and sophisticated.

Industry/Entity Type

Skin Care Product

Logo Text

'omu

Logo styles of interest
Wordmark Logo
Font styles to use
Sans Serif

Requirements
Must have
• This is for a label on a bag, attached images below to show our bag, pouch. We are not sure which color to go with as of yet.
Should not have
• No logo, no need for a mark of any kind.
Not childish or overly girly.

```html
<!DOCTYPE html>
<html lang="en">
<head>
<meta charset="utf-8">
<title>'omu Body Scrub – Label Front and Back</title>
<link href="https://fonts.googleapis.com/css2?family=Josefin+Sans:wght@400;600;700&family=Josefin+Slab:wght@400;600;700&display=swap" rel="stylesheet">
<style>
  :root {
    --canvas: #ffffff;
    --label-paper: #ffffff;
    --pattern-light: #f7f6dc;
    --pattern-mid: #efefc4;
    --ink: #5f5f5f;
    --ink-dark: #545454;
    --shell: #b6b6a8;
  }
  * { margin: 0; padding: 0; box-sizing: border-box; }
  html, body { width: 1200px; height: 1000px; overflow: hidden; background: var(--canvas); }
  .canvas { position: relative; width: 1200px; height: 1000px; }

  .label {
    position: absolute; top: 195px; width: 305px; height: 353px;
    background: var(--label-paper);
  }
  .label--front { left: 170px; }
  .label--back { left: 733px; }

  .label__pattern {
    position: absolute; left: 10px; top: 10px; right: 10px; bottom: 10px;
    background: radial-gradient(ellipse at 50% 40%, var(--pattern-mid), var(--pattern-light) 75%);
  }
  .label__content { position: absolute; inset: 0; color: var(--ink); text-align: center; }

  .brand-name {
    position: absolute; left: 0; right: 0; top: 86px;
    display: flex; align-items: center; justify-content: center; gap: 8px;
    font-family: "Josefin Sans", sans-serif; font-weight: 400;
    font-size: 26px; line-height: 30px; color: var(--ink-dark);
  }
  .brand-name__dot { width: 8px; height: 8px; border-radius: 50%; background: var(--ink-dark); }

  .tagline {
    position: absolute; left: 0; right: 0; top: 165px;
    font-family: "Josefin Sans", sans-serif; font-size: 12px; letter-spacing: 1.5px;
  }
  .product-name {
    position: absolute; left: 0; right: 0; top: 196px;
    font-family: "Josefin Slab", serif; font-weight: 400; font-size: 28px; letter-spacing: 4.5px;
    color: var(--ink-dark); white-space: nowrap;
  }
  .variant {
    position: absolute; left: 0; right: 0; top: 246px;
    font-family: "Josefin Sans", sans-serif; font-size: 12px; letter-spacing: 2px;
  }
  .shell-mark {
    position: absolute; left: 138px; top: 276px; width: 30px; height: 26px;
    background: var(--shell); border-radius: 50% 50% 20% 20%; opacity: .45;
  }
  .weight {
    position: absolute; left: 0; right: 0; top: 320px;
    font-family: "Josefin Slab", serif; font-size: 12px; letter-spacing: 1.5px;
  }

  .back-text {
    font-family: "Josefin Sans", sans-serif; font-weight: 700; text-transform: uppercase;
    white-space: nowrap;
  }
  .intro {
    position: absolute; left: 0; right: 0; top: 152px;
    font-size: 7px; line-height: 9px; letter-spacing: .9px;
  }
  .directions__title {
    position: absolute; left: 0; right: 0; top: 197px;
    font-size: 9.5px; letter-spacing: 1.6px;
  }
  .directions__text {
    position: absolute; left: 0; right: 0; top: 214px;
    font-size: 7.5px; line-height: 10px; letter-spacing: .9px;
  }
  .social {
    position: absolute; left: 34px; top: 268px; text-align: left;
    font-size: 5.5px; letter-spacing: .6px; line-height: 11px;
  }
  .social__item { display: flex; align-items: center; gap: 6px; }
  .social__dot { width: 5px; height: 5px; border-radius: 50%; background: var(--ink-dark); }
  .address {
    position: absolute; left: 202px; top: 268px; text-align: left; font-style: normal;
    font-size: 5.5px; letter-spacing: .6px; line-height: 7.5px;
  }
  .recycle {
    position: absolute; left: 0; right: 0; top: 302px;
    font-size: 5.5px; letter-spacing: .8px;
    display: flex; flex-direction: column; align-items: center; gap: 5px;
  }
</style>
</head>
<body>
<main class="canvas">

  <section class="label label--front" aria-label="Front label">
    <div class="label__pattern" role="img" aria-label="Soft pale yellow watercolour diamond ikat pattern"></div>
    <div class="label__content">
      <div class="brand-name"><span class="brand-name__dot"></span><span>'omu</span></div>
      <p class="tagline">HAWAIIAN SKINCARE</p>
      <h1 class="product-name">BODY SCRUB</h1>
      <p class="variant">CITRUS</p>
      <div class="shell-mark" role="img" aria-label="Small line-drawn seashell emblem"></div>
      <p class="weight">500gm</p>
    </div>
  </section>

  <section class="label label--back" aria-label="Back label">
    <div class="label__pattern" role="img" aria-label="Soft pale yellow watercolour diamond ikat pattern"></div>
    <div class="label__content">
      <p class="intro back-text">'omu's products are made with the finest<br>Hawaiian ingredients to bring you radiating<br>&amp; moisture rich skin without all the nasties.</p>
      <h2 class="directions__title back-text">Directions for use</h2>
      <p class="directions__text back-text">Massage over entire body in the shower<br>and remove with tissue or damp cloth.</p>
      <div class="social back-text">
        <div class="social__item"><span class="social__dot"></span>@'omuskincarehawaii</div>
        <div class="social__item"><span class="social__dot"></span>Like us on Friendpage</div>
      </div>
      <address class="address back-text">'omu Skincare<br>101 Address Rd,<br>Kalapua,<br>Hawaii, XXXX</address>
      <div class="recycle back-text">
        <svg width="7" height="7" viewBox="0 0 8 8" aria-hidden="true">
          <path d="M4 1 L7 6 L1 6 Z" fill="none" stroke="#5f5f5f" stroke-width="1"/>
        </svg>
        <span>Please recycle</span>
      </div>
    </div>
  </section>

</main>
</body>
</html>
```